Law Offices business card

Hi there, I'll need business card for the Law Offices of Tobin Haskell. The information must convey his strategic approach and quick resolution to complex business litigation needs. Please emphasize Civil Litigation, Corporate Law, Business Governance and Real Estate Law. Tobin has over 25 years of experience in these fields.The card should be modern and edgy and the message should be clear. Please consult his current website for ideas.

Business

```html
<!DOCTYPE html>
<html lang="en">
<head>
<meta charset="utf-8">
<title>Law Offices of Tobin Haskell — Business Card</title>
<link rel="stylesheet" href="https://fonts.googleapis.com/css2?family=Open+Sans:wght@400;600;700&display=swap">
<style>
  :root {
    --backdrop: #3a3a3a;
    --card: #050505;
    --ink: #c9c8d6;
    --ink-soft: #9a99a8;
    --accent: #e0302a;
    --rule: #4a4a52;
  }
  * { box-sizing: border-box; margin: 0; padding: 0; }
  html, body { width: 1200px; height: 900px; overflow: hidden; }
  body {
    background: var(--backdrop);
    font-family: "Open Sans", Arial, sans-serif;
    position: relative;
  }
  .card {
    position: absolute;
    width: 620px;
    height: 354px;
    background: var(--card);
    border-radius: 22px;
    overflow: hidden;
    box-shadow: 0 18px 40px rgba(0,0,0,.55);
  }
  .card--front { left: 80px; top: 80px; }
  .card--back { left: 500px; top: 466px; }

  .firm-name {
    position: absolute;
    display: flex;
    align-items: center;
    gap: 12px;
    color: var(--ink);
    font-weight: 600;
    letter-spacing: .5px;
  }
  .firm-name__mark {
    width: 14px; height: 14px;
    background: var(--accent);
    flex: none;
  }
  .card--front .firm-name { left: 70px; top: 128px; font-size: 27px; }
  .card--back .firm-name { left: 40px; top: 66px; font-size: 21px; }

  .rule {
    position: absolute;
    height: 1px;
    background: var(--rule);
  }
  .card--front .rule--mid { left: 250px; right: 0; top: 186px; }
  .card--front .rule--low { left: 0; right: 0; top: 300px; }

  .services {
    position: absolute;
    left: 250px; top: 200px;
    font-size: 13px;
    line-height: 20px;
    letter-spacing: .6px;
    color: var(--ink-soft);
    text-align: center;
    width: 280px;
  }
  .services .services__key { color: var(--accent); }

  .card--back .rule--top { left: 330px; right: 22px; top: 36px; }
  .card--back .rule--name { left: 262px; right: 22px; top: 218px; }

  .contact {
    position: absolute;
    right: 28px; top: 52px;
    list-style: none;
    font-size: 14px;
    line-height: 22px;
    color: var(--ink);
    text-align: right;
  }
  .contact li { display: flex; align-items: center; justify-content: flex-end; gap: 8px; }
  .contact svg { width: 11px; height: 11px; fill: var(--accent); flex: none; }

  .person {
    position: absolute;
    left: 40px; top: 202px;
  }
  .person__name {
    font-size: 21px;
    font-weight: 700;
    color: var(--ink);
    letter-spacing: .3px;
  }
  .person__title {
    font-size: 12px;
    font-weight: 600;
    color: var(--accent);
    letter-spacing: 1px;
    margin-left: 22px;
  }
  .address {
    position: absolute;
    left: 60px; top: 282px;
    font-size: 14px;
    line-height: 21px;
    color: var(--ink-soft);
    font-style: normal;
  }
</style>
</head>
<body>

<section class="card card--front" aria-label="Card front">
  <div class="firm-name"><span class="firm-name__mark"></span>Law Offices of Tobin Haskell, PA</div>
  <div class="rule rule--mid"></div>
  <p class="services">
    BUSINESS LITIGATION<br>
    <span class="services__key">REAL ESTATE</span><br>
    TITLE AND CLOSING SERVICES
  </p>
  <div class="rule rule--low"></div>
</section>

<section class="card card--back" aria-label="Card back">
  <div class="rule rule--top"></div>
  <div class="firm-name"><span class="firm-name__mark"></span>Law Offices of Tobin Haskell, PA</div>

  <ul class="contact">
    <li>555-014-2136
      <svg viewBox="0 0 24 24"><path d="M6.6 10.8a15 15 0 0 0 6.6 6.6l2.2-2.2c.3-.3.7-.4 1-.2 1.1.4 2.3.6 3.6.6.6 0 1 .4 1 1V20c0 .6-.4 1-1 1A17 17 0 0 1 3 4c0-.6.4-1 1-1h3.5c.6 0 1 .4 1 1 0 1.3.2 2.5.6 3.6.1.3 0 .7-.2 1z"/></svg>
    </li>
    <li>555-014-2367
      <svg viewBox="0 0 24 24"><path d="M7 1h10a2 2 0 0 1 2 2v18a2 2 0 0 1-2 2H7a2 2 0 0 1-2-2V3a2 2 0 0 1 2-2zm0 3v14h10V4zm5 15.5a1 1 0 1 0 0 2 1 1 0 0 0 0-2z"/></svg>
    </li>
    <li>tobin@haskelllaw.com
      <svg viewBox="0 0 24 24"><path d="M2 5h20v14H2zm2 2v.4l8 5 8-5V7zm0 2.8V17h16V9.8l-8 5z"/></svg>
    </li>
    <li>www.haskelllaw.com
      <svg viewBox="0 0 24 24"><path d="M12 2a10 10 0 1 0 0 20 10 10 0 0 0 0-20zm6.9 9h-3a15 15 0 0 0-1.4-6.2A8 8 0 0 1 18.9 11zM12 4c.9 1.2 1.8 3.6 1.9 7h-3.8c.1-3.4 1-5.8 1.9-7zM9.5 4.8A15 15 0 0 0 8.1 11h-3a8 8 0 0 1 4.4-6.2zM5.1 13h3a15 15 0 0 0 1.4 6.2A8 8 0 0 1 5.1 13zm6.9 7c-.9-1.2-1.8-3.6-1.9-7h3.8c-.1 3.4-1 5.8-1.9 7zm2.5-.8a15 15 0 0 0 1.4-6.2h3a8 8 0 0 1-4.4 6.2z"/></svg>
    </li>
  </ul>

  <div class="rule rule--name"></div>
  <div class="person">
    <h1 class="person__name">TOBIN HASKELL</h1>
    <p class="person__title">ATTORNEY</p>
  </div>

  <address class="address">
    118B Harbor Avenue<br>
    Lake Vista, FL 33410
  </address>
</section>

</body>
</html>
```